Bodywork Quietude Business Card Design

I want to create a very elegant and sophisticated two sided business card for my massage practice (www.bodyworkquietude.net). I have attached the logo and a PDF with some ideas down for the back of the card but I am open to suggestions. I will want to tie in a post card and flyer to the card later.
Similar colors to website would be great.
Target Market(s)
High end clientele, people looking for a sophisticated spa experience.
Industry/Entity Type
Massage
Contact Information for Business Card
Bodywork Quietude
7318 Larkspur Ave S, Suite 305
Seattle, WA 98103
(206) 555-0147
www.bodyworkquietude.net
Look and feel

```html
<!DOCTYPE html>
<html lang="en">
<head>
<meta charset="utf-8">
<title>Bodywork Quietude – Business Card</title>
<link rel="stylesheet" href="https://fonts.googleapis.com/css2?family=Tinos&display=swap">
<style>
  :root{
    --stage:#b9b9b9;
    --ink:#1d3340;
    --text:#2a2320;
    --white:#ffffff;
    --orchid-light:#f3f1ef;
    --orchid-shade:#e2dcd8;
    --orchid-accent:#d9b8d0;
    --skin-deep:#b8683a;
    --skin-mid:#d1895a;
    --mat:#e2b48f;
    --bloom:#f6dcc0;
    --band:rgba(255,244,236,0.82);
  }
  *{box-sizing:border-box;margin:0;padding:0}
  html,body{width:1200px;height:1200px;overflow:hidden}
  body{
    background:var(--stage);
    font-family:"Tinos","Times New Roman",serif;
    color:var(--text);
    display:flex;flex-direction:column;align-items:center;justify-content:center;gap:60px;
  }
  .card{
    position:relative;width:900px;height:514px;overflow:hidden;
    box-shadow:0 10px 24px rgba(0,0,0,.22);
  }
  /* Front */
  .card--front{background:var(--white)}
  .front__orchids{
    position:absolute;inset:0;
    background:
      radial-gradient(ellipse 300px 240px at 92% 8%, var(--orchid-shade), transparent 70%),
      radial-gradient(ellipse 260px 200px at 100% 45%, var(--orchid-accent), transparent 70%),
      radial-gradient(ellipse 320px 260px at 4% 92%, var(--orchid-shade), transparent 70%),
      radial-gradient(ellipse 200px 160px at 0% 60%, var(--orchid-light), transparent 70%),
      var(--white);
  }
  .front__name{
    position:absolute;left:0;right:0;top:196px;text-align:center;
    font-size:58px;letter-spacing:3px;text-transform:uppercase;color:var(--ink);
  }
  .front__service{
    position:absolute;right:150px;bottom:110px;
    font-size:22px;color:var(--text);
  }
  /* Back */
  .back__photo{
    position:absolute;inset:0;
    background:
      radial-gradient(ellipse 240px 300px at 86% 30%, var(--bloom), transparent 70%),
      linear-gradient(100deg, var(--mat) 0 18%, var(--skin-mid) 30%, var(--skin-deep) 55%, var(--skin-mid) 75%, var(--mat) 90%);
  }
  .back__name{
    position:absolute;left:200px;top:170px;
    font-size:40px;letter-spacing:2px;text-transform:uppercase;color:var(--ink);
  }
  .band{position:absolute;background:var(--band);display:flex;flex-direction:column;justify-content:center;gap:10px}
  .band--contact{left:470px;right:0;top:270px;height:110px;padding-left:50px}
  .band--address{left:0;width:560px;top:395px;height:100px;padding-left:80px}
  .line{display:flex;align-items:center;gap:12px;font-size:24px;color:var(--text)}
  .line svg{width:18px;height:18px;flex:none;fill:var(--text)}
  .indent{padding-left:30px}
</style>
</head>
<body>
  <section class="card card--front">
    <div class="front__orchids" role="img" aria-label="Soft photograph of white orchids framing the corners"></div>
    <h1 class="front__name">Bodywork Quietude</h1>
    <p class="front__service">Deep Lomi Ultra Relaxation Massage</p>
  </section>

  <section class="card card--back">
    <div class="back__photo" role="img" aria-label="Photograph of hands giving a back massage beside peach orchids on a bamboo mat"></div>
    <h2 class="back__name">Bodywork Quietude</h2>
    <div class="band band--contact">
      <p class="line">
        <svg viewBox="0 0 24 24" aria-hidden="true"><path d="M6.6 10.8a15.1 15.1 0 0 0 6.6 6.6l2.2-2.2a1 1 0 0 1 1-.25 11.4 11.4 0 0 0 3.6.57 1 1 0 0 1 1 1V20a1 1 0 0 1-1 1A17 17 0 0 1 3 4a1 1 0 0 1 1-1h3.5a1 1 0 0 1 1 1c0 1.25.2 2.45.57 3.57a1 1 0 0 1-.25 1z"/></svg>
        (206) 555-0147
      </p>
      <p class="line">
        <svg viewBox="0 0 24 24" aria-hidden="true"><circle cx="12" cy="12" r="10"/><path d="M2 12h20M12 2c3 3 3 17 0 20M12 2c-3 3-3 17 0 20" stroke="#fff4ec" stroke-width="1.5" fill="none"/></svg>
        www.bodyworkquietude.net
      </p>
    </div>
    <div class="band band--address">
      <p class="line">
        <svg viewBox="0 0 24 24" aria-hidden="true"><path d="M12 2a7 7 0 0 0-7 7c0 5 7 13 7 13s7-8 7-13a7 7 0 0 0-7-7zm0 9.5A2.5 2.5 0 1 1 12 6.5a2.5 2.5 0 0 1 0 5z"/></svg>
        7318 Larkspur Ave S, Suite 305
      </p>
      <p class="line indent">Seattle, WA 98103</p>
    </div>
  </section>
</body>
</html>
```